Brenwick Shield Bundle: Two-Sided laminate to promote our paint, wheel and tire coverage products.

This is a redesign of the example document (Brenwick Shield Bundle Laminate.pdf) for our vehicle protection product package. This will contain the information given in the example on a two-sided document. Colors, fonts, and theme must align with the brand guidelines provided.

Target Market(s)

Middle-class pre-owned vehicle buyers

Industry/Entity Type

Automotive

Font styles to use
Other font styles liked:
• Poppins, Bebas Neue

Requirements
Must have
• Adhere to the color and look of our brand guidelines.
Nice to have
• Good visuals and icons to represent the products in the package.
Should not have
• No cartoon or animated graphics.

```html
<!DOCTYPE html>
<html lang="en">
<head>
<meta charset="utf-8">
<title>Brenwick Shield Bundle – Benefits</title>
<link rel="stylesheet" href="https://fonts.googleapis.com/css2?family=Poppins:wght@500;600;700;800&display=swap">
<style>
  :root {
    --brand-yellow: #F6C619;
    --brand-yellow-deep: #E3B410;
    --ink: #0B0B0B;
    --paper: #FFFFFF;
    --truck-light: #D9DBDC;
    --truck-dark: #7C8083;
  }
  * { box-sizing: border-box; margin: 0; padding: 0; }
  html, body { width: 849px; height: 1200px; overflow: hidden; background: var(--paper); }
  body { font-family: "Poppins", sans-serif; color: var(--ink); }
  .sheet { position: relative; width: 849px; height: 1200px; overflow: hidden; background: var(--paper); }

  .hero-band { position: absolute; left: 0; top: 0; width: 849px; height: 281px; background: var(--brand-yellow); overflow: hidden; }
  .hero-decor { position: absolute; left: 385px; top: 0; width: 464px; height: 270px; background: linear-gradient(200deg, #2A2408 0%, #7A6410 45%, var(--brand-yellow-deep) 80%, var(--brand-yellow) 100%); opacity: 0.55; }
  .dealer-name { position: absolute; left: 53px; top: 80px; font-weight: 800; font-size: 20px; letter-spacing: 1px; text-transform: uppercase; color: var(--ink); line-height: 1; }
  .dealer-place { position: absolute; left: 53px; top: 104px; font-weight: 800; font-size: 9px; letter-spacing: 4px; text-transform: uppercase; color: var(--ink); }
  .page-title { position: absolute; left: 44px; top: 152px; font-weight: 800; font-size: 94px; line-height: 1; letter-spacing: -2px; }

  .section-title { position: absolute; left: 63px; font-weight: 600; font-size: 25px; line-height: 1; }
  .section-title--large { font-size: 27px; }
  .section-sub { position: absolute; left: 63px; font-weight: 600; font-size: 17px; line-height: 1; }

  .benefit { position: absolute; display: flex; align-items: center; gap: 18px; }
  .benefit-icon { width: 54px; height: 54px; flex: none; }
  .benefit-text { font-weight: 700; font-size: 12.5px; line-height: 1.35; }

  .hazard-list { position: absolute; left: 516px; top: 430px; width: 290px; font-weight: 700; font-size: 12.5px; }
  .hazard-list span { position: absolute; white-space: nowrap; }

  .footer-band { position: absolute; left: 0; top: 1100px; width: 849px; height: 100px; background: var(--brand-yellow); }
  .truck-photo { position: absolute; left: 174px; top: 926px; width: 482px; height: 266px; border-radius: 24px; background: linear-gradient(160deg, var(--truck-light) 0%, #B9BCBE 55%, var(--truck-dark) 100%); }
</style>
</head>
<body>
<div class="sheet">
  <svg width="0" height="0" style="position:absolute">
    <defs>
      <symbol id="badge-tick" viewBox="0 0 54 54">
        <rect width="54" height="54" rx="6" fill="#0B0B0B"/>
        <polygon fill="#F6C619" points="27,9 31,13 36.5,11.5 37.5,17 43,19 41.5,24.5 45,29 40.5,32.5 41.5,38 36,38.5 33.5,43.5 28.5,41 23.5,43.5 21,38.5 15.5,38 16.5,32.5 12,29 15.5,24.5 14,19 19.5,17 20.5,11.5 26,13"/>
        <polyline points="20,28 25,33 35,22" fill="none" stroke="#0B0B0B" stroke-width="2.8" stroke-linecap="round" stroke-linejoin="round"/>
      </symbol>
    </defs>
  </svg>

  <header class="hero-band">
    <div class="hero-decor" role="img" aria-label="Decorative black and yellow stripe pattern in the header corner"></div>
    <div class="dealer-name">Brenwick Cars</div>
    <div class="dealer-place">Harlow Ridge</div>
    <h1 class="page-title">BENEFITS</h1>
  </header>

  <h2 class="section-title" style="top:322px">SHEENGUARD Paint Protection</h2>

  <div class="benefit" style="left:63px; top:376px;">
    <svg class="benefit-icon"><use href="#badge-tick"/></svg>
    <p class="benefit-text">Paint repair for covered damages</p>
  </div>
  <div class="benefit" style="left:63px; top:448px;">
    <svg class="benefit-icon"><use href="#badge-tick"/></svg>
    <p class="benefit-text">Reapplication of coating after repairs</p>
  </div>
  <div class="benefit" style="left:444px; top:376px; align-items:flex-start;">
    <svg class="benefit-icon"><use href="#badge-tick"/></svg>
    <p class="benefit-text" style="padding-top:8px">Protects against most environmental<br>hazards such as:</p>
  </div>
  <div class="hazard-list">
    <span style="left:0; top:0">Bird droppings</span>
    <span style="left:107px; top:0">Sun Damage</span>
    <span style="left:211px; top:2px">Tree Sap</span>
    <span style="left:0; top:24px">Hard Water</span>
    <span style="left:87px; top:24px">Insect Damage</span>
    <span style="left:200px; top:25px">Oxidation</span>
    <span style="left:0; top:46px">Road Salt</span>
  </div>

  <h2 class="section-title section-title--large" style="top:531px">Wheel/Rim Warranty</h2>
  <p class="section-sub" style="top:588px">Repair/Replacement for covered damages</p>

  <div class="benefit" style="left:63px; top:622px;">
    <svg class="benefit-icon"><use href="#badge-tick"/></svg>
    <p class="benefit-text">Potholes and other<br>road hazards</p>
  </div>
  <div class="benefit" style="left:322px; top:622px;">
    <svg class="benefit-icon"><use href="#badge-tick"/></svg>
    <p class="benefit-text">Wheel failure<br>or breakdown</p>
  </div>
  <div class="benefit" style="left:581px; top:622px;">
    <svg class="benefit-icon"><use href="#badge-tick"/></svg>
    <p class="benefit-text">Rim unable to<br>hold air</p>
  </div>
  <div class="benefit" style="left:63px; top:699px;">
    <svg class="benefit-icon"><use href="#badge-tick"/></svg>
    <p class="benefit-text">Scratches</p>
  </div>
  <div class="benefit" style="left:322px; top:699px;">
    <svg class="benefit-icon"><use href="#badge-tick"/></svg>
    <p class="benefit-text">Environmental<br>damage</p>
  </div>
  <div class="benefit" style="left:581px; top:699px;">
    <svg class="benefit-icon"><use href="#badge-tick"/></svg>
    <p class="benefit-text">Corrosion</p>
  </div>

  <h2 class="section-title section-title--large" style="top:784px">Nitrogen/Tire Warranty</h2>

  <div class="benefit" style="left:63px; top:832px;">
    <svg class="benefit-icon"><use href="#badge-tick"/></svg>
    <p class="benefit-text">Tire repair/replacement<br>for covered damages</p>
  </div>
  <div class="benefit" style="left:322px; top:832px;">
    <svg class="benefit-icon"><use href="#badge-tick"/></svg>
    <p class="benefit-text">Potholes or other road<br>hazards. Tread depth<br>above 3/32"</p>
  </div>
  <div class="benefit" style="left:581px; top:832px;">
    <svg class="benefit-icon"><use href="#badge-tick"/></svg>
    <p class="benefit-text">Nitrogen inflation refills<br>Unlimited flat repairs</p>
  </div>

  <div class="footer-band"></div>
  <div class="truck-photo" role="img" aria-label="Photo of a light grey full-size pickup truck with black wheels and off-road tires, angled front three-quarter view"></div>
</div>
</body>
</html>
```